Redesign of Form/Document Navigation Page

I need a redesign of our document and navigation bar on the left. We want the same navigation bar layout/setup but want the buttons and typography to be simple and matching all over. The form needs to be aesthetically pleasing and fit within the page.

1st attachment is our Direct Deposit and the second is the form continued.

```html
<!DOCTYPE html>
<html lang="en">
<head>
<meta charset="utf-8">
<title>Employee Direct Deposit Enrollment Form</title>
<link href="https://fonts.googleapis.com/css2?family=Inter+Tight:wght@400;500;600;700&display=swap" rel="stylesheet">
<style>
:root{
  --gold:#e0bb2c;
  --ink:#1a1f2b;
  --slate:#676767;
  --text:#555;
  --white:#fff;
}
*{box-sizing:border-box;margin:0;padding:0}
html,body{width:1123px;height:1200px;overflow:hidden;background:var(--white)}
body{position:relative;font-family:"Inter Tight",Arial,sans-serif;color:var(--text);letter-spacing:-.02em}
.abs{position:absolute}
.brand-panel{left:0;top:0;width:337px;height:422px;background:var(--gold)}
.hero{left:337px;top:0;width:786px;height:422px;background:linear-gradient(100deg,#171c27 0%,#1c2230 55%,#2a303a 80%,#3a3f47 100%)}
.brand-name{left:221px;top:34px;color:var(--white);font-weight:700;font-size:17px;line-height:20px;letter-spacing:-.01em}
.top-nav{left:416px;top:47px;display:flex;gap:42px;font-size:12px;color:var(--white)}
.top-nav span::before{content:"+";color:var(--gold);margin-right:7px}
.user-name{left:826px;top:48px;color:var(--white);font-size:12px}
.user-icon{left:908px;top:41px}
.side-nav{left:175px;top:139px;width:197px;height:336px;background:var(--slate);padding:25px 0 0 21px}
.side-nav li{list-style:none;color:var(--white);font-size:14px;height:33.2px}
.side-nav li.active{color:var(--gold);font-weight:500}
.back-btn{left:196px;top:406px;width:45px;height:45px;border-radius:50%;background:var(--gold);display:flex;align-items:center;justify-content:center}
.hero-title{left:416px;top:133px;color:var(--gold);font-weight:700;font-size:35px;line-height:41px;letter-spacing:-.035em}
.hero-copy{left:418px;top:232px;width:526px;color:var(--white);font-size:11px;line-height:13.5px;letter-spacing:-.03em}
.hero-copy p+p{margin-top:13px}
.btn{background:var(--gold);color:var(--white);font-size:8px;font-weight:700;letter-spacing:.12em;display:flex;align-items:center;justify-content:center;text-transform:uppercase}
.upload{left:418px;top:362px;width:98px;height:26px}
.section-title{left:418px;top:449px;font-size:11px;font-weight:500}
.note{left:418px;top:476px;width:520px;font-size:11px;line-height:13.5px}
.note em{font-style:italic}
.check{display:flex;align-items:center;gap:9px;font-size:7.5px;font-weight:600;letter-spacing:.13em;text-transform:uppercase;color:#444}
.box{width:19px;height:19px;border:1px solid var(--gold)}
.box.on{background:var(--gold)}
.field{border-bottom:2px solid var(--gold);font-size:7.5px;font-weight:600;letter-spacing:.06em;text-transform:uppercase;color:#444;padding:0 0 5px 20px}
.amount{left:682px;top:748px;width:65px;height:19px;background:var(--gold);color:var(--white);font-size:8px;padding-left:20px;display:flex;align-items:center}
.important{left:418px;top:806px;font-size:11px;font-weight:600}
.legal{left:418px;top:833px;width:528px;font-size:11px;line-height:13.5px}
.legal p+p{margin-top:13.5px}
.submit{left:418px;top:1129px;width:130px;height:26px}
</style>
</head>
<body>
<div class="abs brand-panel"></div>
<div class="abs hero" role="img" aria-label="Dark photograph of security cameras mounted on a pole"></div>

<div class="abs brand-name">Northgate<br>Patrol<br>Services</div>

<nav class="abs top-nav"><span>Home</span><span>Help</span></nav>
<div class="abs user-name">Mara Ellison</div>
<svg class="abs user-icon" width="24" width="24" height="24" viewBox="0 0 24 24" fill="none" stroke="#e0bb2c" stroke-width="1.5">
  <circle cx="12" cy="8" r="6"/><path d="M2 22c1-5 5-7 10-7s9 2 10 7z"/>
</svg>

<ul class="abs side-nav">
  <li class="active">Direct Deposit</li>
  <li>Change W-4</li>
  <li>Labour Code</li>
  <li>Personal Information</li>
  <li>Appraisal &amp; Review</li>
  <li>Write Up Slip</li>
  <li>Employee Performance</li>
</ul>
<div class="abs back-btn">
  <svg width="18" height="14" viewBox="0 0 18 14" fill="none" stroke="#fff" stroke-width="2"><path d="M17 7H2M8 1L2 7l6 6"/></svg>
</div>

<h1 class="abs hero-title">Employee Direct&nbsp; Deposit<br>Enrollment Form</h1>
<div class="abs hero-copy">
  <p>To enroll in Direct Deposit, simply fill out a this form. Attach a voided check for each checking account - not a deposit slip. If depositing to a savings account, ask your bank to give you the Routing / Transit Number for your account. It isn't always the same as the number on a savings deposit slip. This will help ensure that you are paid correctly. Once filled out, accounting will review your information for processing. Once processed, you will recieve an email confirmation with details.</p>
  <p>Employees must attach a voided check for each of their accounts to help verify their account numbers and banking routing numbers.</p>
</div>
<div class="abs btn upload">Upload File</div>

<h2 class="abs section-title">Account Information</h2>
<p class="abs note">The last item must be for the remaining amount owed to you. To distribute to more accounts, please complete another form. <em>Make sure to indicate what kind of account, along with enrolling or declining.</em></p>

<div class="abs check" style="left:418px;top:534px"><span class="box on"></span>New Enrollment</div>
<div class="abs check" style="left:549px;top:533px"><span class="box"></span>Change Enrollment</div>
<div class="abs check" style="left:693px;top:533px"><span class="box"></span>Cancel Enrollment</div>

<div class="abs field" style="left:418px;top:609px;width:218px">Bank Name</div>
<div class="abs field" style="left:681px;top:609px;width:87px">City</div>
<div class="abs field" style="left:813px;top:609px;width:86px">State</div>
<div class="abs field" style="left:418px;top:673px;width:218px">Routing Transit Number</div>
<div class="abs field" style="left:682px;top:673px;width:218px">Account Number</div>

<div class="abs check" style="left:419px;top:749px"><span class="box"></span>Checking</div>
<div class="abs check" style="left:549px;top:749px"><span class="box"></span>Savings</div>
<div class="abs amount">100 &nbsp;%</div>
<div class="abs check" style="left:760px;top:754px">Amount</div>

<h3 class="abs important">Important! Please read and sign before completing and submitting.</h3>
<div class="abs legal">
  <p>I hereby authorize NORTHGATE PATROL SERVICES to deposit any amounts owed me, as instructed by my employer, by initiating credit entries to my account at the financial institution (hereinafter "Bank") indicated on this form. Further, I authorize Bank to accept and to credit any credit entries indicated by NORTHGATE PATROL SERVICES to my account. In the even that NORTHGATE PATROL SERVICES deposits funds erroneously into my account. I authorize NORTHGATE PATROL SERVICES to debit my account for an amount not to exceed the original amount of the erroneous credit.</p>
  <p>This authorization is to remain in full force and effect until NORTHGATE PATROL SERVICES and Bank have recieved written notice from me of its termination in such time and in such manner as to afford NORTHGATE PATROL SERVICES and Bank reasonable opportunity to act on it.</p>
</div>

<div class="abs field" style="left:418px;top:1022px;width:218px">Employee Name</div>
<div class="abs field" style="left:681px;top:1022px;width:218px">Employee Signature</div>
<div class="abs field" style="left:681px;top:1073px;width:218px">Sign Date</div>

<div class="abs btn submit">Submit Document</div>
</body>
</html>
```